Realtor Card Design

Im a realtor that represents buyers and sellers and want a card that has a modern look to it. I also work with a loan officer and want the back of the card to read " Get qualified now to buy your dream home!" I also would like the logo I sent to be on the front of the card but not preference on where exactly. If i could see samples with it in different places that would be great. I work out of the greater Houston area.I would like to incorporate a patriotic theme in my cards so red, white and blue are preferred.
Updates

Sorry for the delayed response, the logo I had included does not have to be on the card.As long as the company name is included with all the other info and some sort if logo what matters. I will extend the dealine to give more time for submissions. I would also like to see a few versions of cards with a watermark of the american flag in the background. I want to stay away from white backgrounds.Please keep the designs coming. Thank you.                                    

Industry/Entity Type

Realtor

Contact Information for Business Card

Cobalt Ridge Realty
Wade Lindqvist (555)732-4186
email: wlindqvistrealtor@quorvex.com
www.plenwick.com/WadeLindqvist

Requirements
Must have
• Must include the logo and the basic contact info i've given.

```html
<!DOCTYPE html>
<html lang="en">
<head>
<meta charset="utf-8">
<title>Cobalt Ridge Realty – Business Card</title>
<link rel="stylesheet" href="https://fonts.googleapis.com/css2?family=Cinzel:wght@600&family=Questrial&display=swap">
<style>
  :root {
    --navy: #1c1f45;
    --navy-deep: #14163a;
    --red: #e3222b;
    --white: #ffffff;
    --flag-grey: #e4e6ec;
    --page: #ecebe8;
  }
  html, body {
    margin: 0;
    width: 1200px;
    height: 784px;
    overflow: hidden;
    background: var(--page);
  }
  .canvas {
    position: relative;
    width: 1200px;
    height: 784px;
  }
  .card {
    position: absolute;
    width: 540px;
    height: 308px;
    overflow: hidden;
    box-shadow: 0 6px 18px rgba(0,0,0,0.18);
    background: radial-gradient(ellipse at 60% 40%, #262a58 0%, var(--navy) 55%, var(--navy-deep) 100%);
  }
  .card--back { left: 70px; top: 100px; }
  .card--front { left: 590px; top: 376px; }

  .back-tagline {
    position: absolute;
    left: 40px;
    top: 158px;
    margin: 0;
    font-family: "Questrial", "Century Gothic", sans-serif;
    font-size: 21px;
    letter-spacing: 0.3px;
    color: var(--red);
  }

  .front-header {
    position: absolute;
    left: 0; top: 0;
    width: 100%;
    height: 132px;
    background: linear-gradient(160deg, var(--white) 0%, var(--flag-grey) 45%, var(--white) 70%, #eceef3 100%);
  }
  .company-name {
    position: absolute;
    left: 0; right: 0;
    top: 48px;
    margin: 0;
    text-align: center;
    font-family: "Cinzel", "Trajan Pro", serif;
    font-weight: 600;
    font-size: 33px;
    letter-spacing: 0.5px;
    color: var(--navy);
  }
  .front-stripe {
    position: absolute;
    left: 0; top: 132px;
    width: 100%;
    height: 8px;
    background: var(--red);
  }
  .agent {
    position: absolute;
    left: 38px;
    top: 150px;
    font-family: "Questrial", "Century Gothic", sans-serif;
  }
  .agent-name {
    margin: 0;
    font-size: 21px;
    font-weight: 700;
    color: var(--red);
  }
  .agent-title {
    margin: 2px 0 0 8px;
    font-size: 13px;
    color: var(--white);
  }
  .contact-list {
    list-style: none;
    margin: 12px 0 0 0;
    padding: 0;
  }
  .contact-item {
    display: flex;
    align-items: center;
    gap: 10px;
    height: 25px;
    font-size: 18px;
    color: var(--white);
  }
  .contact-icon { width: 16px; height: 16px; flex: none; }
</style>
</head>
<body>
<main class="canvas">

  <section class="card card--back" aria-label="Card back">
    <p class="back-tagline">Get qualified now to buy your dream home!</p>
  </section>

  <section class="card card--front" aria-label="Card front">
    <div class="front-header" role="img" aria-label="Faint waving American flag watermark in white and grey"></div>
    <h1 class="company-name">Cobalt Ridge Realty</h1>
    <div class="front-stripe"></div>

    <div class="agent">
      <p class="agent-name">Wade Lindqvist</p>
      <p class="agent-title">Manager</p>
      <ul class="contact-list">
        <li class="contact-item">
          <svg class="contact-icon" viewBox="0 0 16 16" aria-hidden="true">
            <path fill="var(--red)" d="M3.6 1.2l2.3 2.6-1.3 1.6c.9 2 2.3 3.4 4.2 4.3l1.6-1.3 2.6 2.3-1.4 2.2C6.5 12.6 3.3 9.4 1.3 2.6z"/>
          </svg>
          (555)732-4186
        </li>
        <li class="contact-item">
          <svg class="contact-icon" viewBox="0 0 16 16" aria-hidden="true">
            <rect x="1" y="3.5" width="14" height="10" rx="1.5" fill="var(--red)"/>
            <path d="M1.8 4.5L8 9.3l6.2-4.8" fill="none" stroke="var(--navy)" stroke-width="1.4"/>
          </svg>
          wlindqvistrealtor@quorvex.com
        </li>
        <li class="contact-item">
          <svg class="contact-icon" viewBox="0 0 16 16" aria-hidden="true">
            <g fill="none" stroke="var(--red)" stroke-width="1.4">
              <circle cx="8" cy="8" r="6.5"/>
              <ellipse cx="8" cy="8" rx="2.8" ry="6.5"/>
              <path d="M1.5 8h13M2.6 4.6h10.8M2.6 11.4h10.8"/>
            </g>
          </svg>
          www.plenwick.com/WadeLindqvist
        </li>
      </ul>
    </div>
  </section>

</main>
</body>
</html>
```